Tavenlume: Smart Quotes for Wine Lovers

Hello. I am completing book of quotes for wine lovers. Need the text formatted so that it is easy to read and aesthetically pleasing...modern, clean, smart. Number the pages. The cover is complete. Book is small square. 7.5 by 7.5 inches. If you want to show me first few pages that would be awesome. Thank you!
Updates

I edited the quotes so if you downloaded first ones, please grab these ones instead, thank you! 

Target Market(s)

wine lovers. Urban. Modern.

Industry/Entity Type

Quotes

Requirements
Should not have
• No color. black and white only.

```html
<!DOCTYPE html>
<html lang="en">
<head>
<meta charset="utf-8">
<title>Tavenlume – Smart Quotes for Wine Lovers</title>
<link rel="stylesheet" href="https://fonts.googleapis.com/css2?family=Philosopher:wght@700&family=Marcellus&display=swap">
<style>
  :root {
    --backdrop: #e4e4e4;
    --paper: #ffffff;
    --ink: #111111;
    --gutter: #444444;
    --glass-front: #c4c4c4;
    --glass-back: #e6e6e6;
    --shadow: rgba(0, 0, 0, 0.35);
  }
  * { margin: 0; padding: 0; box-sizing: border-box; }
  html, body {
    width: 1200px;
    height: 900px;
    overflow: hidden;
    background: var(--backdrop);
  }
  .spread {
    position: absolute;
    left: 60px;
    top: 187px;
    width: 1067px;
    height: 531px;
    display: flex;
    background: var(--paper);
    box-shadow: 4px 4px 6px var(--shadow);
  }
  .page {
    position: relative;
    width: 50%;
    height: 100%;
    color: var(--ink);
    text-align: center;
  }
  .page + .page { border-left: 1px solid var(--gutter); }
  .quote {
    position: absolute;
    left: 30px;
    right: 30px;
    font-family: "Philosopher", "Trebuchet MS", sans-serif;
    font-weight: 700;
    font-size: 26px;
    line-height: 33px;
    letter-spacing: 0.2px;
  }
  .page--first .quote { top: 48px; }
  .page--second .quote { top: 62px; }
  .glass-art {
    position: absolute;
    left: 50%;
    top: 206px;
    width: 68px;
    height: 168px;
    transform: translateX(-50%);
    border-radius: 10px;
    background: linear-gradient(160deg, var(--glass-back), var(--glass-front));
  }
  .bio {
    position: absolute;
    left: 20px;
    right: 20px;
    top: 393px;
    font-family: "Marcellus", Georgia, serif;
    font-size: 13.5px;
    line-height: 18px;
  }
  .bio-name { font-weight: 700; font-family: "Philosopher", "Trebuchet MS", sans-serif; }
  .folio {
    position: absolute;
    left: 0;
    right: 0;
    top: 492px;
    font-family: "Philosopher", "Trebuchet MS", sans-serif;
    font-weight: 700;
    font-size: 13px;
  }
</style>
</head>
<body>
  <main class="spread">
    <section class="page page--first">
      <p class="quote">The discovery of a good wine is<br>increasingly better for mankind<br>than the discovery of a new star.<br>– Lorenzo da Verrano</p>
      <div class="glass-art" role="img" aria-label="Two overlapping grey wine glass icons"></div>
      <p class="bio"><span class="bio-name">Lorenzo di Paolo da Verrano</span> (1461 –1527)<br>Tuscan Court Painter, Sculptor, Architect, Lutenist,<br>Astronomer, Surveyor, Engineer, Glassmaker, Botanist,<br>Mapmaker, Vintner and Poet.</p>
      <p class="folio">-1-</p>
    </section>
    <section class="page page--second">
      <p class="quote">Be careful to trust a person who<br>does not like wine.<br>– Konrad Mertens</p>
      <div class="glass-art" role="img" aria-label="Two overlapping grey wine glass icons"></div>
      <p class="bio"><span class="bio-name">Konrad Mertens (1824 –1891)</span><br>Prussian Essayist, Economist, Teacher, Historian, Journalist,<br>and Wine Merchant.</p>
      <p class="folio">-2-</p>
    </section>
  </main>
</body>
</html>
```